Webbanner-Design für Slideshow
Zielgruppe
Annegret bietet 3 Kurse an:
diese Kurse verhelfen einem selbst seine Schutzengel wieder zu hören,
mit ihnen ihren Seelenplan weshalb man auf Erden ist zu sehen,
sowie professionell umzusetzen.
Zielgruppe:
Spirituelle Menschen,
welche Engel lieben,
an sich mental gerne in Kursen & Privat arbeiten,
neues Wissen sich liebend gerne aneignen,
ihren Seelenplan wissen und umsetzen möchten,
die Schönheit im Inneren (Seele) und
im Aussen (Körper & Umgebung) lieben.
Aufgabenstellung
Produktbannerbild für meine Website (Slideshow):
Hintergrund: vorhanden in Form von einem Jpeg, hier auf diesem Foto bitte dich einfach mit folgendem beschäftigen:
Schriftzug groß: Engel (wieder) hören lernen & deinen Seelenplan umsetzen
mit Annegret Holzmeier (klein, oder großer Schriftzug?)
Schriftzug klein: mehr …
Schriftfarbe: weiss
Schriftart: moderne Schrift (z.Bsp. was die Zeitschriften benützen)
Haus Button Schriftzug: KURSE IN MUC
Buttons Ideen, Vierecke oder Kreise ect.: Transparent bitte und in passender Farbe
Stil: Modern, klar, schön, nicht verschnörkelt, unesoterisch, unverspielt
Mein Logo mit Flügel: irgendwo miteinbauen
Sonstiges: anbei noch ein Iconzeichen für Kurse Seminar
Auflösung Farbe: Text & Icons für Druck (Flyer) & Webproduktpräsentation (Slideshow)
Maße: (bei 1600xca.872 px., bleiben, Banner nicht verkleinern, oder ranzoomen)

```html
<!DOCTYPE html>
<html lang="de">
<head>
<meta charset="utf-8">
<title>Engel hören lernen – Annegret Holzmeier</title>
<link href="https://fonts.googleapis.com/css2?family=Advent+Pro:wght@300;400&family=Tulpen+One&display=swap" rel="stylesheet">
<style>
  :root {
    --white: #ffffff;
    --panel: rgba(222, 128, 134, 0.62);
    --rule: rgba(255, 255, 255, 0.85);
    --scene-light: #f4ece9;
    --scene-mid: #e8d6d2;
    --scene-warm: #d9b8ae;
    --floor: #c79f86;
  }
  html, body {
    margin: 0;
    padding: 0;
    width: 1200px;
    height: 638px;
    overflow: hidden;
    background: var(--scene-light);
  }
  .banner {
    position: relative;
    width: 1200px;
    height: 638px;
    overflow: hidden;
  }
  .banner__backdrop {
    position: absolute;
    inset: 0;
    background:
      linear-gradient(180deg, transparent 0%, transparent 78%, var(--floor) 100%),
      radial-gradient(ellipse at 45% 40%, var(--scene-light) 0%, var(--scene-mid) 55%, var(--scene-warm) 100%);
  }
  .banner__panel {
    position: absolute;
    left: 660px;
    top: 21px;
    width: 518px;
    height: 465px;
    background: var(--panel);
    color: var(--white);
    text-shadow: 0 1px 3px rgba(120, 60, 60, 0.45);
  }
  .headline {
    margin: 0;
    position: absolute;
    left: 0;
    right: 0;
    top: 14px;
    font-family: "Advent Pro", sans-serif;
    font-weight: 300;
    font-size: 50px;
    line-height: 78px;
    letter-spacing: 1px;
    text-align: center;
  }
  .rule {
    position: absolute;
    left: 13px;
    width: 490px;
    height: 1px;
    background: var(--rule);
  }
  .rule--top { top: 248px; }
  .rule--bottom { top: 376px; }
  .presenter {
    position: absolute;
    left: 0;
    right: 0;
    top: 252px;
    margin: 0;
    font-family: "Tulpen One", sans-serif;
    font-weight: 400;
    font-size: 104px;
    line-height: 120px;
    text-align: center;
    white-space: nowrap;
  }
  .more {
    position: absolute;
    left: 24px;
    top: 396px;
    display: flex;
    align-items: center;
    gap: 12px;
    font-family: "Advent Pro", sans-serif;
    font-weight: 400;
    font-size: 30px;
    color: var(--white);
    text-decoration: none;
  }
  .brand {
    display: flex;
    align-items: center;
    gap: 6px;
    font-family: "Advent Pro", sans-serif;
    font-weight: 400;
    font-size: 20px;
  }
</style>
</head>
<body>
  <main class="banner">
    <div class="banner__backdrop" role="img" aria-label="Foto: Frau am weißen Schreibtisch in hellem Raum mit Blumen, Kaminsims und Herzrahmen"></div>

    <section class="banner__panel">
      <h1 class="headline">Engel (wieder) hören<br>lernen &amp; einen<br>Seelenplan umsetzen.</h1>
      <div class="rule rule--top"></div>
      <p class="presenter">Mit Annegret Holzmeier</p>
      <div class="rule rule--bottom"></div>
      <a class="more" href="#">
        <span>mehr...</span>
        <span class="brand">
          <svg width="14" height="14" viewBox="0 0 14 14" aria-hidden="true"><circle cx="7" cy="7" r="6" fill="none" stroke="#ffffff" stroke-width="1.5"/></svg>
          seelenweg
        </span>
      </a>
    </section>
  </main>
</body>
</html>
```